Saffron Lotus Court Business Card

I am looking for a business card desgined for my restaurant. It is an Indian restaurant, we are looking for something thats modern, yet traditional with the indian culture, we are looking for colors that match our logo. The logo is a design of the building with the name of the restaurant. for more information on the restaurant go to www.saffronlotuscourt.example

Industry/Entity Type

Indian Restaurant

Contact Information for Business Card

we are looking for somthing thats modern, yet traditional with the indian culture, we are looking for colors that match our logo. The logo is a design of the building with the name of the restaurant. for more information on the restaurant go to www.saffronlotuscourt.example

Requirements
Must have
• The logo that is attached,
• Name: Harjot Banwal,
• address of the restaurant: 2917 West Tamarind Ave, Phoenix, Arizona, 85047
• Phone: (602) 517-3094
• Fax: (602) 768-2145
• Restaurant Catering Banquet
• Website: www.SaffronLotusCourt.example
Nice to have
• wanted to get something that goes with the theme of the restaurant, which is traditional but also keep a very professional and modern touch

```html
<!DOCTYPE html>
<html lang="en">
<head>
<meta charset="utf-8">
<title>Saffron Lotus Court Business Card</title>
<link href="https://fonts.googleapis.com/css2?family=Source+Sans+3:wght@400;600&display=swap" rel="stylesheet">
<style>
  :root {
    --backdrop: #3b322d;
    --card: #1f2226;
    --accent-red: #c8352a;
    --accent-orange: #e0622a;
    --text-light: #d8d8d8;
    --rule: #8a8a8a;
    --foil-silver: #cfd2d5;
  }
  * { margin: 0; padding: 0; box-sizing: border-box; }
  html, body {
    width: 1200px; height: 769px; overflow: hidden;
    background: var(--backdrop);
    font-family: "Source Sans 3", sans-serif;
  }
  .stage {
    position: relative; width: 1200px; height: 769px;
    display: flex; align-items: center; justify-content: center; gap: 60px;
  }
  .card {
    position: relative; width: 500px; height: 286px;
    background: var(--card);
    box-shadow: 0 10px 30px rgba(0,0,0,.45);
    overflow: hidden;
  }
  .brand-name {
    font-weight: 600; text-transform: uppercase; text-align: center;
    letter-spacing: 2px; line-height: 1.05;
  }
  .card-front .brand-name {
    position: absolute; top: 32px; right: 34px; width: 150px;
    color: var(--accent-red); font-size: 24px;
  }
  .card-front .divider {
    position: absolute; top: 136px; left: 180px; right: 30px;
    height: 1px; background: var(--rule);
  }
  .address {
    position: absolute; top: 148px; right: 30px; text-align: left;
    color: var(--text-light); font-size: 13px; line-height: 1.4;
  }
  .person {
    position: absolute; left: 30px; bottom: 20px;
  }
  .person-name { color: var(--accent-red); font-size: 17px; font-weight: 600; line-height: 1.15; }
  .person-role { color: var(--accent-orange); font-size: 13.5px; line-height: 1.3; }
  .person .short-rule { width: 170px; height: 1px; background: var(--rule); margin: 6px 0 5px; }
  .contact-list { list-style: none; }
  .contact-list li {
    display: flex; align-items: center; gap: 9px;
    color: var(--text-light); font-size: 13px; line-height: 1.4;
  }
  .contact-list svg { width: 11px; height: 11px; fill: var(--accent-red); flex: none; }
  .card-back { display: flex; align-items: center; justify-content: center; }
  .card-back .brand-name { color: var(--foil-silver); font-size: 34px; width: 220px; }
</style>
</head>
<body>
<main class="stage">
  <section class="card card-front">
    <div class="brand-name">Saffron Lotus Court</div>
    <div class="divider"></div>
    <p class="address">2917 West Tamarind Ave<br>Phoenix, Arizona, 85047</p>
    <div class="person">
      <p class="person-name">Harjot Banwal</p>
      <p class="person-role">Restaurant Catering Banquet</p>
      <div class="short-rule"></div>
      <ul class="contact-list">
        <li><svg viewBox="0 0 12 12" aria-hidden="true"><path d="M2.5 1l2 2.2-1 1.3c.7 1.5 1.8 2.6 3.3 3.3l1.3-1 2.2 2-1.2 1.7C5.3 10.5 1.5 6.7 1 2.2z"/></svg>(602) 517-3094</li>
        <li><svg viewBox="0 0 12 12" aria-hidden="true"><rect x="3" y="1" width="6" height="3"/><rect x="1" y="4.5" width="10" height="5" rx="1"/><rect x="3" y="9.5" width="6" height="1.5"/></svg>(602) 768-2145</li>
        <li><svg viewBox="0 0 12 12" aria-hidden="true"><circle cx="6" cy="6" r="5.5"/><path d="M1 6h10M6 .5c-2 2.5-2 8.5 0 11M6 .5c2 2.5 2 8.5 0 11" stroke="#1f2226" stroke-width=".8" fill="none"/></svg>www.SaffronLotusCourt.example</li>
      </ul>
    </div>
  </section>
  <section class="card card-back">
    <div class="brand-name">Saffron Lotus Court</div>
  </section>
</main>
</body>
</html>
```